Wellness, weight management medical practice

We have a logo but want help designing and finalizing the business card. Japanese name. Will eventually be a holistic, full-service weight management and wellness center. Will be a virtual only practice to start.

```html
<!DOCTYPE html>
<html lang="en">
<head>
<meta charset="utf-8">
<title>Sorami Wellness – Business Card</title>
<link rel="stylesheet" href="https://fonts.googleapis.com/css2?family=Lato:wght@400;700;900&family=Noto+Sans+JP:wght@400;700&display=swap">
<style>
  :root {
    --bg-dark: #1c1c1c;
    --bg-mid: #3d3d3d;
    --card-black: #232323;
    --card-white: #ffffff;
    --gold: #a8782a;
    --gold-light: #c99a3e;
    --ink: #1d1d1d;
  }
  * { margin: 0; padding: 0; box-sizing: border-box; }
  html, body { width: 1200px; height: 875px; overflow: hidden; }
  body {
    background: linear-gradient(160deg, var(--bg-mid) 0%, var(--bg-dark) 100%);
    font-family: "Lato", sans-serif;
    position: relative;
  }
  .card {
    position: absolute;
    left: 260px;
    width: 680px;
    height: 388px;
    border-radius: 22px;
    box-shadow: 0 18px 40px rgba(0,0,0,.45);
    overflow: hidden;
  }
  .card--back { top: 30px; background: var(--card-black); }
  .card--front { top: 452px; background: var(--card-white); }

  /* brand name */
  .brand {
    position: absolute;
    color: var(--gold-light);
    font-family: "Lato", sans-serif;
    font-weight: 400;
    letter-spacing: .18em;
    text-transform: uppercase;
    white-space: nowrap;
  }
  .card--back .brand { left: 50%; top: 50%; transform: translate(-50%, -50%); font-size: 30px; }
  .card--front .brand { right: 40px; top: 40px; font-size: 15px; color: var(--gold); }

  /* front layout */
  .rule {
    position: absolute;
    left: 40px; right: 40px; top: 222px;
    height: 1.5px;
    background: var(--gold);
  }
  .identity { position: absolute; left: 40px; bottom: 172px; }
  .identity__name {
    color: var(--gold);
    font-weight: 900;
    font-size: 34px;
    letter-spacing: -.01em;
    line-height: 1;
  }
  .identity__role {
    color: var(--gold-light);
    font-size: 20px;
    margin-top: 4px;
  }
  .identity-jp { position: absolute; right: 40px; bottom: 172px; text-align: right; font-family: "Noto Sans JP", sans-serif; }
  .identity-jp__name { color: var(--gold); font-weight: 700; font-size: 28px; line-height: 1.1; }
  .identity-jp__role { color: var(--gold-light); font-size: 14px; letter-spacing: .08em; margin-top: 4px; }

  .contact, .address { position: absolute; top: 240px; list-style: none; color: var(--ink); }
  .contact { left: 40px; font-size: 18px; }
  .contact li { display: flex; align-items: center; gap: 10px; line-height: 27px; }
  .address { right: 40px; text-align: right; font-size: 16px; }
  .address li { display: flex; justify-content: flex-end; gap: 10px; line-height: 24px; }
  .address li.jp { font-family: "Noto Sans JP", sans-serif; margin-top: 10px; }
  .icon { width: 14px; height: 14px; fill: var(--gold-light); flex: none; }
  .icon--pin { margin-top: 5px; }
</style>
</head>
<body>

  <section class="card card--back" aria-label="Card back">
    <div class="brand">Sorami Wellness</div>
  </section>

  <section class="card card--front" aria-label="Card front">
    <div class="brand">Sorami Wellness</div>

    <div class="identity-jp">
      <div class="identity-jp__name">ハナ・ソラミ</div>
      <div class="identity-jp__role">ウェルネスプラクティス</div>
    </div>

    <div class="identity">
      <div class="identity__name">HANA SORAMI</div>
      <div class="identity__role">Wellnes Practice</div>
    </div>

    <div class="rule"></div>

    <ul class="contact">
      <li><svg class="icon" viewBox="0 0 16 16"><path d="M3.6 1.5l2.3 2.6-1.3 1.8c.9 2 2.5 3.6 4.5 4.5l1.8-1.3 2.6 2.3-1.5 2.1C6.5 13.3 2.7 9.5 1.5 3z"/></svg>(123) 456-7890</li>
      <li><svg class="icon" viewBox="0 0 16 16"><path d="M4 1h8v14H4zM5.5 2.5v9h5v-9z"/></svg>(231) 456-7890</li>
      <li><svg class="icon" viewBox="0 0 16 16"><path d="M1 3h14v10H1zM2.5 4.5L8 9l5.5-4.5z"/></svg>office@soramiwellness.com</li>
      <li><svg class="icon" viewBox="0 0 16 16"><circle cx="8" cy="8" r="7"/><path d="M1 8h14M8 1c2.5 2.5 2.5 11.5 0 14M8 1c-2.5 2.5-2.5 11.5 0 14" stroke="#fff" stroke-width="1" fill="none"/></svg>www.soramiwellness.com</li>
    </ul>

    <ul class="address">
      <li><span>Your Address, City<br>State, Zip 1235</span><svg class="icon icon--pin" viewBox="0 0 16 16"><path d="M8 1a5 5 0 015 5c0 3.5-5 9-5 9S3 9.5 3 6a5 5 0 015-5zm0 3a2 2 0 100 4 2 2 0 000-4z"/></svg></li>
      <li class="jp"><span>あなたの住所、市<br>州、郵便番号 1235</span><svg class="icon icon--pin" viewBox="0 0 16 16"><path d="M8 1a5 5 0 015 5c0 3.5-5 9-5 9S3 9.5 3 6a5 5 0 015-5zm0 3a2 2 0 100 4 2 2 0 000-4z"/></svg></li>
    </ul>
  </section>

</body>
</html>
```